Wordpress Business Travel Blog and Discussion Board

Oh, Hello!

We are looking for a motivated designer to create a full, turnkey interactive WordPress website geared toward business travel that includes a news style blog (look at GizmoForge.com and Wirelume.com for the style we like) that is seamlessly integrated with a robust message board (look at JetBanter.com and AirTally.com). Ok, so stick with us here because this is actually a pretty cool project that shouldn't be too hard, but yes, of course we have some curve balls that we are throwing your way. Sorry! :)

*On the front page*

- We would like to have a typical news style blog layout that is fun, somewhat professional, and easy to read. That's easy!

- Somewhere within first glance, we would like to have a short list of the most active discussions on our discussion board. (What's trending, or something like that). Not too bad, right?

- Overall, want to have a good amount of content, but we also do not want the visitor to feel as if he or she is having to sift through a lot of content to see what he or she wants to see. Great! We're past the beginning!

We will have traditional visual advertising on all of our pages. Please leave space as necessary :)

*On the Blog/News story pages*

Let's keep these simple - but there is a twist!

Let's say I create a blog/news post. I would like that blog/news post to also be opened as a discussion on the discussion board. For example, I write an article about Corvane Airways and their service on a particular international flight. This will be opened as a discussion under the Corvane Airways topic in the discussion board. Other users can also open new discussions under any topic on the discussion board, but they cannot post stories (unless permission is given) to the blog wall. We would like their posts to show up as regular discussion board posts while the news/blog posts by us show up as news/blog posts on the front page, *and* (oh yes we did!) as discussions in the discussion board. Of course, users will still be able to post comments to the news/blog post, which will also be posted in the discussion.

OK, does that make sense? Let me know if I can help make this more clear! :) Sorry!

*Wiki Pages*

Take a look at the Corvane Airways example above. In that example, my news/blog entry automatically opens a new discussion post. Although we won't necessarily need to create a new wiki page, we would like to tag the post and the discussion to a wiki page about the topic. The wiki page can be created and edited by all users (and locked by us if necessary). BONUS! Can we tag more than one wiki page?

*Websites that inspire us*

GizmoForge.com - concept and design
Wirelume.com - concept and design
JetBanter.com - concept
AirTally.com - concept
pipwhisper.com - concept

All of the sites above are great and we can only thrive with their great success. We are not aiming to be a competitor to the travel sites, but just another great option for interested visitors. Please do not simply copy what they have. What is posted above is a list of our favorite sites that we visit every day.

Our favorite font is Segoe UI, but please don't use this (or a similar font) too much! Maybe just titles would be great. You're the designer so you can make the call here.

Also, our favorite color is blue, but if you have another favorite color, go ahead and show us what you can do! (Don't use too much blue!)

*Oh, and One More Thing*

(I know, you thought we were done. We're not!)

Here's the killer - We would like to create a way for people to, say, enter the details of their next trip and be matched with someone who will also be on a portion of their trip.

For example, let's say I am flying Halvern Skyways flight 109 from Los Angeles to New York Pellham Airport this Friday. I am staying at the Marlowe Inn Harbor Plaza on Friday night, and I am flying back on Saturday night on Brisko flight 290 from New York Pellham airport back to Los Angeles. Another user will also be on the Brisko flight back to Los Angeles with me and he entered that information in the website. (Note, the user has to manually enter this information). The other user and I will both be notified that there is at least one other user who will be on the same Brisko flight as me. We will both have the option to reveal our online identity - which will in fact be released to each person as long as each person *mutually* agrees.

This can be very simple - almost like a dating site type of match but it is based on two people being in the same place at the same time (based on what they report). Also, we would like to be able to collect this information - not necessarily tied to the user's true identity. The information we would like to have is - what the user is claiming he or she is doing on the trip (i.e. staying at the Marlowe Harbor Plaza, flying Halvern Skyways), and whether or not the user agreed to reveal his or her identity - AND! whether or not the users both revealed their identity.

*Most Important*

HAVE FUN and THANK YOU!! :)

A couple of quick notes - this is a design and code project. We are most likely offering a more $(!) design and code project for the version 2.0 of this website once we get user feedback from this first round.

Also, the name of the website is GoJaunt. (www.gojaunt.example)

Good luck!

Reason: Extending as requested by a few designers. Only 3 more days to get your designs in!

Reason: All designs look great! Last chance for one or two more designers who have requested an extension. All designs that were already submitted on time will be considered with much higher priority. Thank you!

Requirements
Must have
• We need to have a high end, professional, modern, and clean design on the front page to entice readers to constantly visit and stay on our site.
Nice to have
• It would be great to give us the ability to automatically recognize users for visiting the website and/or participating and commenting. Social badges, recognition, etc. would be very cool.
Should not have
• Although this is a website around business travel, we do not necessarily want it to be business travel themed. There can be hints of the theme, but otherwise the visual look should be somewhat generic.

```html
<!DOCTYPE html>
<html lang="en">
<head>
<meta charset="utf-8">
<title>GoJaunt — Business Travel Blog</title>
<link href="https://fonts.googleapis.com/css2?family=Open+Sans:wght@400;600;700&family=Arimo:wght@400;700&display=swap" rel="stylesheet">
<style>
:root{
  --page:#e9e9e9;
  --blue:#1d6eaa;
  --blue-mid:#2f82c2;
  --blue-dark:#0f4c7c;
  --blue-deep:#0b3f69;
  --link:#1a74b8;
  --ink:#222;
  --text:#555;
  --muted:#888;
  --line:#dcdcdc;
  --card:#ececec;
  --white:#fff;
  --orange:#f39a1e;
  --green:#6fb52c;
}
*{box-sizing:border-box;margin:0;padding:0}
html,body{width:696px;height:1200px;overflow:hidden}
body{position:relative;background:var(--page);font-family:"Arimo",Arial,sans-serif;color:var(--text)}
.abs{position:absolute}
a{color:inherit;text-decoration:none}

/* header */
.topnav{left:92px;top:0;width:521px;height:15px;background:var(--blue);display:flex;justify-content:center;gap:12px;font-size:7.5px;color:var(--white);line-height:15px}
.masthead{left:84px;top:15px;width:529px;height:42px;background:var(--blue)}
.brand-band{left:86px;top:17px;width:348px;height:38px;border:1px solid #9cc6e6;background:linear-gradient(90deg,#2d8fd0 0%,#7cc1ec 45%,#c8e6f8 70%,#5aa6dc 100%)}
.logo{left:95px;top:22px;font:700 21px/28px "Open Sans",sans-serif;color:var(--white)}
.search{left:445px;top:28px;width:162px;height:14px;background:var(--white);border-radius:7px;font-size:7px;color:var(--muted);line-height:14px;padding-left:8px}
.search-btn{right:0;top:0;width:16px;height:14px;border-radius:0 7px 7px 0;background:var(--green)}
.subnav{left:0;top:57px;width:696px;height:13px;background:linear-gradient(#f7f7f7,#d9d9d9);border-bottom:1px solid #c8c8c8}
.subnav-links{left:90px;top:57px;height:13px;display:flex;gap:15px;font-size:7.5px;color:var(--link);line-height:13px}
.account{left:505px;top:57px;width:98px;height:12px;background:var(--blue-mid);border-radius:3px;font-size:7.5px;color:var(--white);line-height:12px;display:flex;gap:9px;padding-left:8px}

/* columns */
.main{left:84px;top:70px;width:351px;height:1075px;background:var(--white);box-shadow:0 0 3px rgba(0,0,0,.25)}
.sidebar{left:435px;top:70px;width:178px;height:1085px;background:var(--blue-mid)}

/* featured */
.feature-title{left:90px;top:75px;width:175px;font:700 12.5px/14px "Open Sans",sans-serif;color:#333}
.player{left:90px;top:107px;width:173px;height:134px;background:linear-gradient(135deg,#d94a5a 0%,#e9b7a6 40%,#6e8fb0 75%,#c93a3a 100%);border:1px solid #bbb}
.player-bar{left:0;bottom:0;width:100%;height:13px;background:#e4e4e4;font-size:6.5px;color:#333;line-height:13px}
.highlights-head{left:270px;top:73px;width:160px;height:17px;border-bottom:2px solid #555;font:700 10px/13px "Open Sans",sans-serif;color:var(--link)}
.hl-card{left:270px;width:159px;height:46px;background:var(--card);border-radius:3px}
.hl-thumb{left:3px;top:5px;width:50px;height:36px;background:linear-gradient(135deg,#3c6f9e,#b9d3e8 60%,#5a86ad)}
.hl-text{left:59px;top:5px;width:92px;font-size:7.5px;line-height:10px;color:#444}
.view-all{left:300px;top:252px;width:128px;text-align:right;font:600 9px/12px "Open Sans",sans-serif;color:var(--link)}
.rule{left:90px;width:339px;height:1px;background:var(--line)}

/* posts */
.bubble{left:92px;width:33px;height:12px;border-radius:6px;background:#6aa3d3;color:var(--white);font-size:7px;line-height:12px;text-align:center}
.social-row{left:92px;height:11px;display:flex;gap:2px;font-size:6px;line-height:9px}
.social-btn{border:1px solid #c4cfdc;background:#eef2f7;border-radius:2px;padding:0 3px;color:#333;font-weight:700}
.social-count{border:1px solid #ccc;background:var(--white);padding:0 3px;color:#555}
.byline{left:156px;font-size:6.5px;line-height:8px}
.byline b{color:var(--link);font-weight:700;display:block}
.post-title{left:156px;width:272px;font:700 16.5px/17px "Open Sans",sans-serif;color:#111}
.photo{left:156px;border:1px solid #ccc}
.body-side{left:282px;width:147px;font-size:7.1px;line-height:10.8px;color:#666}
.body-full{left:156px;width:273px;font-size:7.1px;line-height:10.8px;color:#666}
.more{color:var(--link);font-weight:700}
.caption{left:60px;top:126px;width:150px;height:26px;background:rgba(40,40,40,.7);border-radius:3px;color:var(--white);font-size:7px;line-height:26px;padding-left:28px}
.caption::before{content:"";position:absolute;left:12px;top:8px;border-left:9px solid var(--white);border-top:5px solid transparent;border-bottom:5px solid transparent}
.next{left:90px;top:1119px;width:339px;height:20px;background:var(--blue-mid);color:var(--white);font:700 12px/20px "Open Sans",sans-serif;text-align:right;padding-right:12px}

/* sidebar widgets */
.ad{left:441px;top:76px;width:166px;height:139px;background:linear-gradient(#f7a62a,#ef8a12);border:1px solid #fff}
.ad-line1{left:0;top:14px;width:100%;text-align:center;font:700 13.5px/15px "Open Sans",sans-serif;color:#231a12}
.ad-line2{left:0;top:52px;width:100%;text-align:center;font:700 13.5px/15px "Open Sans",sans-serif;color:#231a12}
.ad-roll{left:66px;top:68px;font:700 10px/12px "Open Sans",sans-serif;color:#231a12}
.ad-photo{left:8px;top:84px;width:58px;height:54px;background:linear-gradient(#d6bfa2,#7f8a5a)}
.ad-brand{left:74px;top:108px;width:86px;height:28px;background:var(--white);border-radius:2px;text-align:center;font:700 10px/16px "Open Sans",sans-serif;color:#333}
.ad-brand small{display:block;font:400 5px/6px "Arimo",sans-serif;color:#555}
.widget{left:440px;width:168px;background:var(--white)}
.widget-head{height:18px;background:linear-gradient(#fff,#e6e6e6);border-bottom:1px solid #d0d0d0;padding-left:6px;font:700 8.5px/18px "Open Sans",sans-serif;color:var(--blue)}
.field-label{left:6px;font-size:7.5px;color:#444}
.field{left:64px;width:72px;height:13px;border:1px solid #bbb;background:var(--white)}
.btn{background:var(--blue);color:var(--white);font-size:7.5px;font-weight:700;text-align:center}
.tabs{left:0;top:0;width:168px;height:26px;display:flex;background:#d9d9d9;overflow:hidden}
.tab{width:56px;flex:none;font:400 8px/9px "Open Sans",sans-serif;color:#888;padding:5px 0 0 12px;border-left:1px solid #c5c5c5}
.tab.active{background:var(--white);color:var(--link);border-left:none}
.trend{left:10px;width:152px;height:54px;border-bottom:1px solid #eee}
.trend-thumb{left:1px;top:6px;width:49px;height:38px;border:1px solid #ccc;background:linear-gradient(135deg,#dfe9f2,#7a98b4 55%,#26384f)}
.trend-text{left:59px;top:4px;width:92px;font-size:8.5px;line-height:9.3px;color:#222}
.icon-sq{top:118px;width:24px;height:24px;border-radius:4px}
.copyright{right:91px;top:1179px;font-size:7.5px;line-height:9px;color:#b8cde0;white-space:nowrap}
</style>
</head>
<body>

<nav class="abs topnav"><a>Home</a><a>Blog</a><a>Forums</a><a>Members</a><a>Wiki</a><a>Help</a></nav>
<header class="abs masthead"></header>
<div class="abs brand-band" role="img" aria-label="Sky banner with an airliner in flight"></div>
<div class="abs logo">GoJaunt</div>
<div class="abs search">Search<span class="abs search-btn"></span></div>
<div class="abs subnav"></div>
<nav class="abs subnav-links"><a>Miles &amp; Points</a><a>Travel &amp; Dining</a><a>Community</a><a>ORVO</a><a>Destinations</a></nav>
<div class="abs account"><a>Register Now</a><a>Login</a></div>

<main class="abs main"></main>
<aside class="abs sidebar"></aside>

<!-- featured video -->
<h2 class="abs feature-title">Nullam ac lectus nisi, id commodo sem.</h2>
<div class="abs player">
  <div class="abs" style="left:0;top:0;width:100%;height:120px" role="img" aria-label="Video still of a family travelling together on an airport escalator"></div>
  <div class="abs player-bar">
    <svg class="abs" style="left:5px;top:3px" width="80" height="7" viewBox="0 0 80 7"><path d="M0 0L6 3.5L0 7Z" fill="#222"/><path d="M14 2h2l3-2v7l-3-2h-2z" fill="#222"/><rect x="26" y="2.5" width="50" height="2" fill="#1d6eaa"/><circle cx="76" cy="3.5" r="2.5" fill="#222"/></svg>
    <span class="abs" style="left:92px">42:15</span><span class="abs" style="left:117px">Share</span>
    <svg class="abs" style="left:145px;top:3px" width="22" height="7" viewBox="0 0 22 7"><circle cx="3.5" cy="3.5" r="2.6" fill="none" stroke="#222" stroke-width="1"/><rect x="12" y="0.5" width="9" height="6" fill="none" stroke="#222"/></svg>
  </div>
</div>
<h3 class="abs highlights-head">HIGHLIGHTS</h3>
<div class="abs hl-card" style="top:94px"><div class="abs hl-thumb" role="img" aria-label="Airport terminal interior"></div><p class="abs hl-text">Lorem ipsum dolor sit amet, consectetur adipiscing elit.</p></div>
<div class="abs hl-card" style="top:146px"><div class="abs hl-thumb" role="img" aria-label="Business traveller with a laptop"></div><p class="abs hl-text">Maecenas sit amet massa metus, id semper diam.</p></div>
<div class="abs hl-card" style="top:198px"><div class="abs hl-thumb" role="img" aria-label="Traveller with luggage in a lounge"></div><p class="abs hl-text">Donec feugiat ligula non odio ullamcorper nec luctus turpis vehicula.</p></div>
<a class="abs view-all">View all videos ›</a>
<div class="abs rule" style="top:270px"></div>

<!-- post 1 -->
<div class="abs bubble" style="top:285px">18</div>
<div class="abs social-row" style="top:302px"><span class="social-btn">Like</span><span class="social-count">251</span></div>
<div class="abs social-row" style="top:317px"><span class="social-btn">Post</span><span class="social-count">483</span></div>
<div class="abs social-row" style="top:332px"><span class="social-btn">Share</span><span class="social-count">21</span></div>
<div class="abs social-row" style="top:347px"><span class="social-btn">+1</span><span class="social-count">17</span></div>
<p class="abs byline" style="top:284px"><b>OWEN HARTLEY</b>posted 51 mins ago</p>
<h2 class="abs post-title" style="top:303px">Fusce commodo ligula consequat lacus venenatis congue condimentum neque auctor.</h2>
<div class="abs photo" style="top:378px;width:116px;height:92px;background:linear-gradient(#6b6f86,#c9a58a 55%,#d8b28b 70%,#5d5a6a)" role="img" aria-label="Airliner flying against a sunset sky"></div>
<p class="abs body-side" style="top:377px">Sed ut perspiciatis unde omnis iste natus error sit voluptatem accusantium doloremque laudantium, totam rem aperiam, eaque ipsa quae ab illo inventore veritatis et quasi architecto beatae vitae dicta sunt explicabo. Nemo enim ipsam voluptatem quia voluptas sit aspernatur aut odit aut fugit, sed quia consequuntur magni dolores eos qui</p>
<p class="abs body-full" style="top:479px">Sed ut perspiciatis unde omnis iste natus error sit voluptatem accusantium doloremque laudantium, totam rem aperiam, eaque ipsa quae ab illo inventore veritatis et quasi architecto beatae vitae dicta sunt explicabo. Nemo enim ipsam voluptatem quia voluptas sit aspernatur aut odit aut fugit, sed quia consequuntur magni dolores eos qui ratione voluptatem sequi nesciunt. Neque porro quisquam est, qui dolorem <a class="more">⟶Read More</a></p>
<div class="abs rule" style="top:556px"></div>

<!-- post 2 -->
<div class="abs bubble" style="top:576px">6</div>
<div class="abs social-row" style="top:592px"><span class="social-btn">Like</span><span class="social-count">251</span></div>
<div class="abs social-row" style="top:607px"><span class="social-btn">Post</span><span class="social-count">483</span></div>
<div class="abs social-row" style="top:622px"><span class="social-btn">Share</span><span class="social-count">21</span></div>
<div class="abs social-row" style="top:637px"><span class="social-btn">+1</span><span class="social-count">17</span></div>
<p class="abs byline" style="top:574px"><b>NADIA CREST</b>posted yesterday</p>
<h2 class="abs post-title" style="top:594px">Donec volutpat dapibus lacus, in convallis magna aliquam in.</h2>
<div class="abs photo" style="top:641px;width:116px;height:92px;background:linear-gradient(135deg,#dbe8f2,#8fb0c9 50%,#3f4c5e)" role="img" aria-label="Business travellers walking through an airport concourse"></div>
<p class="abs body-side" style="top:640px">Sed ut perspiciatis unde omnis iste natus error sit voluptatem accusantium doloremque laudantium, totam rem aperiam, eaque ipsa quae ab illo inventore veritatis et quasi architecto beatae vitae dicta sunt explicabo. Nemo enim ipsam voluptatem quia voluptas sit aspernatur aut odit aut fugit, sed quia consequuntur magni dolores eos qui ratione voluptatem sequi nesciunt. Neque porro quisquam <a class="more">⟶Read More</a></p>
<div class="abs rule" style="top:773px"></div>

<!-- post 3 -->
<div class="abs bubble" style="top:792px">6</div>
<div class="abs social-row" style="top:809px"><span class="social-btn">Like</span><span class="social-count">251</span></div>
<div class="abs social-row" style="top:824px"><span class="social-btn">Post</span><span class="social-count">483</span></div>
<div class="abs social-row" style="top:839px"><span class="social-btn">Share</span><span class="social-count">21</span></div>
<div class="abs social-row" style="top:854px"><span class="social-btn">+1</span><span class="social-count">17</span></div>
<p class="abs byline" style="top:790px"><b>NADIA CREST</b>posted yesterday</p>
<h2 class="abs post-title" style="top:810px">Phasellus consectetur erat nec tortor lobortis sed vestibulum massa tristique.</h2>
<div class="abs photo" style="top:868px;width:268px;height:163px;background:linear-gradient(#d9d3cb,#a79d92 55%,#4a4a4e)">
  <div class="abs" style="left:0;top:0;width:100%;height:100%" role="img" aria-label="Video still of two business travellers waiting in an airport lounge"></div>
  <div class="abs caption">Sed ut perspiciatis unde omnis</div>
</div>
<p class="abs body-full" style="top:1040px">Sed ut perspiciatis unde omnis iste natus error sit voluptatem accusantium doloremque laudantium, totam rem aperiam, eaque ipsa quae ab illo inventore veritatis et quasi architecto beatae vitae dicta sunt explicabo. Nemo enim ipsam voluptatem quia voluptas sit aspernatur aut odit aut fugit, sed quia consequuntur magni dolores eos qui ratione voluptatem sequi nesciunt. Neque porro quisquam <a class="more">⟶Read More</a></p>
<a class="abs next">Next ›</a>

<!-- sidebar -->
<div class="abs ad">
  <p class="abs ad-line1">LEELA MOSS IS A<br>BUSINESS PIONEER</p>
  <p class="abs ad-line2">WHAT ABOUT YOU?</p>
  <p class="abs ad-roll">&lt;&lt;Rollover</p>
  <div class="abs ad-photo" role="img" aria-label="Portrait photo of an entrepreneur"></div>
  <div class="abs ad-brand">NameNest<small>Domains, Websites and more...</small></div>
</div>

<section class="abs widget" style="top:222px;height:82px">
  <h3 class="widget-head">MATCH A PORTION ON YOUR TRIP!</h3>
  <span class="abs field-label" style="top:30px">Start Date</span><div class="abs field" style="top:27px"></div>
  <svg class="abs" style="left:145px;top:27px" width="13" height="13" viewBox="0 0 13 13"><rect x="0.5" y="1.5" width="12" height="11" rx="1" fill="#d8ebf8" stroke="#3b8ccc"/><rect x="0.5" y="1.5" width="12" height="3" fill="#3b8ccc"/></svg>
  <span class="abs field-label" style="top:49px">Flight Number</span><div class="abs field" style="top:46px"></div>
  <svg class="abs" style="left:143px;top:49px" width="18" height="8" viewBox="0 0 18 8"><path d="M1 4h16M9 1l4 3-4 3M4 2l2 2-2 2" stroke="#555" stroke-width="1.2" fill="none"/></svg>
  <div class="abs btn" style="left:64px;top:65px;width:36px;height:12px;line-height:12px">Search</div>
</section>

<section class="abs widget" style="top:311px;height:305px">
  <div class="abs tabs"><span class="tab active">Recent<br>Trending</span><span class="tab">Archieve<br>Trending</span><span class="tab">All<br>Trending</span></div>
  <div class="abs trend" style="top:32px"><div class="abs trend-thumb" role="img" aria-label="Business traveller at an airport window"></div><p class="abs trend-text">Maecenas sit amet massa metus, id semper diam.</p></div>
  <div class="abs trend" style="top:86px"><div class="abs trend-thumb" role="img" aria-label="Business traveller at an airport window"></div><p class="abs trend-text">Maecenas sit amet massa metus, id semper diam.</p></div>
  <div class="abs trend" style="top:140px"><div class="abs trend-thumb" role="img" aria-label="Business traveller at an airport window"></div><p class="abs trend-text">Maecenas sit amet massa metus, id semper diam.</p></div>
  <div class="abs trend" style="top:194px"><div class="abs trend-thumb" role="img" aria-label="Business traveller at an airport window"></div><p class="abs trend-text">Maecenas sit amet massa metus, id semper diam.</p></div>
  <div class="abs trend" style="top:248px;border:none"><div class="abs trend-thumb" role="img" aria-label="Business traveller at an airport window"></div><p class="abs trend-text">Maecenas sit amet massa metus, id semper diam.</p></div>
</section>

<section class="abs widget" style="top:622px;height:54px">
  <h3 class="widget-head">NEWSLETTERS</h3>
  <div class="abs" style="left:6px;top:28px;width:102px;height:16px;border:1px solid #bbb;font-size:7px;line-height:14px;padding-left:5px;color:#555">Enter your e-mail address</div>
  <div class="abs btn" style="left:108px;top:28px;width:54px;height:16px;line-height:16px;background:var(--blue-mid);font-weight:400">Subscribe</div>
</section>

<section class="abs widget" style="top:684px;height:154px">
  <h3 class="widget-head">SOCIALIZE</h3>
  <div class="abs social-btn" style="left:12px;top:33px;font-size:6px;line-height:11px;height:13px">Like</div>
  <p class="abs" style="left:50px;top:33px;width:112px;font-size:5.8px;line-height:7px;color:#555">498,909 people like this. Sign Up to see what your friends like.</p>
  <div class="abs social-btn" style="left:14px;top:76px;height:16px;font-size:7px;line-height:14px;padding:0 5px">Follow @GoJaunt</div>
  <div class="abs social-count" style="left:92px;top:76px;height:16px;font-size:7px;line-height:14px;font-weight:700;color:#333;border-radius:2px">2.3M followers</div>
  <div class="abs icon-sq" style="left:10px;background:#3b5a98"></div>
  <div class="abs icon-sq" style="left:40px;background:#4ab0d6"></div>
  <div class="abs icon-sq" style="left:70px;background:#2a78a8"></div>
  <div class="abs icon-sq" style="left:100px;background:#d6332a"></div>
  <div class="abs icon-sq" style="left:131px;background:#f0731e"></div>
</section>

<!-- footer -->
<footer>
  <div class="abs" style="left:92px;top:1155px;width:521px;height:15px;background:var(--blue-dark)"></div>
  <nav class="abs" style="left:98px;top:1155px;height:15px;display:flex;gap:20px;font-size:7.5px;line-height:15px;color:var(--white)"><a>Home</a><a>Blog</a><a>Forums</a><a>Members</a><a>Wiki</a><a>Help</a></nav>
  <div class="abs" style="left:92px;top:1170px;width:521px;height:30px;background:var(--blue-deep)"></div>
  <div class="abs" style="left:97px;top:1173px;font:700 15px/22px 'Open Sans',sans-serif;color:#d8e6f2">GoJaunt</div>
  <p class="abs copyright">Privacy Policy &nbsp;&nbsp;|&nbsp;&nbsp; Terms Of Service &nbsp;&nbsp;|&nbsp;&nbsp; © 2012 GoJaunt. All rights reserved.</p>
</footer>

</body>
</html>
```